Website Design for Business Law Firm

We have a logo and now we would like a web site design for our new website. Our small firm provides creative and aggressive transactional (not litigation) legal services to advise healthcare, technology, internet-based and traditional companies and investors in such companies on healthcare, technology, financing, mergers/acquisitions, real estate and other transactions, legal compliance and general corporate and business matters.

We would like to see a website design that is professional and appropriate for executives, professionals, investors and government regulators to visit, that conveys professionalism and competence while being a little edgy and modern - no typical legal motifs such as gavels, books, or scales of justice. We advise businesses and investors and guide them through complicated issues quickly, capably and differently from other law firms. We are part of the business team and get things done.

The logo is attached, and we like gray as a color to complement it. The intention of the logo is to convey that in a storm or challenging time, people come to this firm, and people come to this firm when they need the power and disruption to change things or shake them up.

I have also enclosed a picture of our business card for consideration.

On the other hand, you can check out the current simple site at www.venhollow.example to see we have used a space motif in the past to evoke that we help create stars (the nebula featured there). This is not a necessary part of the new website and it may look better without it.

We appreciate your creativity and look forward to designs.

Industry/Entity Type

Business

Requirements
Must have
• We anticipate the following pages, and you may submit different ideas for the different pages:
• 1. Landing page
• 2. Services pages - healthcare, IT/Technology, general counsel services, financings, mergers/acquisitions, mediation/arbitration, procurement and productization
• 3. About Us including contact information
• Our name and contact information:
• Quellane Law Firm, P.C.
• 8716 SW 19th Ave.
• Portland, OR 97213
• phone: 971.555.0143
• fax: 971.555.0187
Nice to have
• Please consider designs that enhance the impressions we are looking for
Should not have
• Please no gavels, scales of justice, law books, or similar traditional legal imagery.

```html
<!DOCTYPE html>
<html lang="en">
<head>
<meta charset="utf-8">
<title>Quellane Law Firm, P.C.</title>
<link rel="stylesheet" href="https://fonts.googleapis.com/css2?family=Arimo:wght@400;700&family=Roboto+Condensed:wght@400;700&display=swap">
<style>
  :root {
    --page-bg: #d3d3d3;
    --panel-top: #3b3b3b;
    --panel-bottom: #1c1c1c;
    --band: #0a0a0a;
    --rule: #6a6a6a;
    --rule-faint: rgba(255,255,255,0.08);
    --text: #ffffff;
    --text-soft: #e6e6e6;
    --caption-bg: #575757;
    --hero-light: #9a9a9a;
    --hero-dark: #1f1f1f;
  }
  * { box-sizing: border-box; margin: 0; padding: 0; }
  html, body { width: 1200px; height: 913px; overflow: hidden; }
  body { background: var(--page-bg); position: relative; font-family: "Roboto Condensed", "Arial Narrow", sans-serif; color: var(--text); }

  .site {
    position: absolute; left: 46px; top: 37px; width: 1107px; height: 836px;
    border-radius: 16px; overflow: hidden;
    background: linear-gradient(to bottom, var(--panel-top) 0, #2e2e2e 45%, var(--panel-bottom) 80%);
    box-shadow: 0 2px 6px rgba(0,0,0,0.35);
  }
  .top-band { position: absolute; left: 0; top: 0; width: 100%; height: 26px; background: var(--band); border-bottom: 2px solid #555; }

  .brand {
    position: absolute; left: 16px; top: 25px; width: 374px; height: 89px;
    display: flex; align-items: center; gap: 18px; padding-left: 6px;
  }
  .brand-mark { width: 16px; height: 16px; background: var(--text); }
  .brand-name { font-size: 46px; font-weight: 400; letter-spacing: 8px; color: var(--text); }

  .main-nav { position: absolute; right: 31px; top: 97px; display: flex; }
  .main-nav a {
    color: var(--text); text-decoration: none; font-weight: 700; font-size: 18px;
    padding: 0 0 0 40px; margin-left: 0; position: relative;
  }
  .main-nav a + a { margin-left: 26px; }
  .main-nav a + a::before {
    content: ""; position: absolute; left: 0; top: -5px; width: 1px; height: 22px; background: #777;
  }
  .nav-rule { position: absolute; left: 16px; top: 129px; width: 1060px; height: 1px; background: var(--rule); }

  .firm-title { position: absolute; left: 16px; top: 153px; font-family: "Arimo", Arial, sans-serif; font-weight: 700; font-size: 22px; letter-spacing: 0.5px; }
  .firm-tagline { position: absolute; left: 16px; top: 179px; font-size: 17px; color: var(--text-soft); }

  .service-list { position: absolute; left: 0; top: 232px; width: 1107px; list-style: none; }
  .service-list li {
    height: 23.7px; line-height: 22px; padding-left: 16px; font-size: 16px; color: var(--text-soft);
    border-bottom: 1px solid var(--rule-faint);
  }

  .hero { position: absolute; left: 389px; top: 154px; width: 687px; height: 452px; box-shadow: 0 6px 10px rgba(0,0,0,0.45); }
  .hero-image {
    position: absolute; left: 0; top: 0; width: 687px; height: 366px;
    background: radial-gradient(ellipse at 55% 45%, var(--hero-light) 0, #5e5e5e 45%, var(--hero-dark) 100%);
  }
  .hero-title { position: absolute; left: 38px; top: 29px; font-family: "Arimo", Arial, sans-serif; font-weight: 700; font-size: 18px; }
  .hero-arrow { position: absolute; top: 180px; }
  .hero-arrow.prev { left: 12px; }
  .hero-arrow.next { right: 22px; }
  .hero-caption {
    position: absolute; left: 0; top: 366px; width: 687px; height: 86px; background: var(--caption-bg);
    padding: 17px 12px 0 20px; font-family: "Arimo", Arial, sans-serif; font-size: 11px; line-height: 13.5px;
  }

  .footer { position: absolute; left: 0; top: 671px; width: 100%; height: 165px; background: var(--band); border-top: 3px solid #8a8a8a; }
  .contact-block { position: absolute; top: 30px; font-weight: 700; font-size: 14.5px; line-height: 19px; }
  .contact-block h2 { font-size: 18px; font-weight: 700; margin-bottom: 4px; line-height: 22px; }
  .contact-visit { left: 417px; }
  .contact-call { left: 742px; }
  .contact-mail { left: 961px; }
  .footer-icon { position: absolute; }
  .footer-divider { position: absolute; top: 33px; width: 1px; height: 78px; background: #777; }
</style>
</head>
<body>
<div class="site">
  <div class="top-band"></div>

  <div class="brand">
    <span class="brand-mark"></span>
    <span class="brand-name">QUELLANE</span>
  </div>

  <nav class="main-nav">
    <a href="#">HOME</a>
    <a href="#">ABOUT</a>
    <a href="#">SOLUTIONS</a>
  </nav>
  <div class="nav-rule"></div>

  <h1 class="firm-title">LAW FIRM, P.C.</h1>
  <p class="firm-tagline">Pragmatic, Creative Service for Innovative Business</p>

  <ul class="service-list">
    <li>Strategic Alliances</li>
    <li>Business Relationships</li>
    <li>Outsourcing</li>
    <li>Procurements - Buying or Selling</li>
    <li>Licensing and Technology Exploitation</li>
    <li>Venture Financing</li>
    <li>Creative Private Financing Arrangements</li>
    <li>Mergers and Acquistions</li>
    <li>Real Estate</li>
    <li>Contract</li>
    <li>Audits, Analyses ad Legal Project Management</li>
    <li>Local Counsel for transactions and Due Diligence</li>
    <li>Vendor Management</li>
    <li>Dispute Resolution</li>
    <li>Service as Mediator or Arbitrator</li>
  </ul>

  <section class="hero">
    <div class="hero-image" role="img" aria-label="Photo of coins, banknotes, a pen and a financial report with a line chart"></div>
    <h2 class="hero-title">Headline News Update</h2>
    <svg class="hero-arrow prev" width="14" height="26" viewBox="0 0 14 26"><polygon points="14,0 0,13 14,26" fill="#fff"/></svg>
    <svg class="hero-arrow next" width="14" height="26" viewBox="0 0 14 26"><polygon points="0,0 14,13 0,26" fill="#fff"/></svg>
    <p class="hero-caption">Lorem ipsum dolor sit amet, consectetuer adipiscing elit, sed diam nonummy nibh euismod tincidunt ut laoreet dolore magna aliquam erat volutpat. Ut wisi enim ad minim veniam, quis nostrud exerci tation ullamcorper suscipit lobortis nisl ut aliquip ex ea commodo consequat. Duis autem vel eum iriure dolor in hendrerit in vulputate velit esse molestie consequat, vel illum dolore eu feugiat nulla facilisis at vero eros et accumsan e</p>
  </section>

  <footer class="footer">
    <svg class="footer-icon" style="left:372px;top:28px" width="24" height="50" viewBox="0 0 24 50">
      <path d="M12 0 A12 12 0 0 1 24 12 C24 18 17 22 12 50 C7 22 0 18 0 12 A12 12 0 0 1 12 0 Z" fill="#fff"/>
      <circle cx="12" cy="12" r="5" fill="#0a0a0a"/>
    </svg>
    <div class="contact-block contact-visit">
      <h2>Visit</h2>
      <p>Quellane Law Firm, P.C.,<br>P.O.BOX 5082, Portland, OR 97213</p>
    </div>
    <div class="footer-divider" style="left:658px"></div>

    <svg class="footer-icon" style="left:676px;top:28px" width="50" height="38" viewBox="0 0 50 38">
      <path d="M6 2 L14 0 L20 10 L15 15 C19 23 25 28 32 31 L37 26 L48 31 L46 38 C30 40 8 26 2 10 Z" fill="#fff"/>
    </svg>
    <div class="contact-block contact-call">
      <h2>Call</h2>
      <p>971.555.0143 phone<br>971.555.0187 fax</p>
    </div>
    <div class="footer-divider" style="left:890px"></div>

    <svg class="footer-icon" style="left:904px;top:32px" width="42" height="28" viewBox="0 0 42 28">
      <rect x="1" y="1" width="40" height="26" fill="none" stroke="#fff" stroke-width="2"/>
      <polyline points="1,1 21,16 41,1" fill="none" stroke="#fff" stroke-width="2"/>
      <line x1="1" y1="27" x2="16" y2="12" stroke="#fff" stroke-width="2"/>
      <line x1="41" y1="27" x2="26" y2="12" stroke="#fff" stroke-width="2"/>
    </svg>
    <div class="contact-block contact-mail">
      <h2>Contact</h2>
      <p>info@quellane.example</p>
    </div>
  </footer>
</div>
</body>
</html>
```